Digital Album Cover - Where The Quiet River Bends (Piano & Cello)

HiI would like a digital album coverTitle: "Where The Quiet River Bends (Piano & Cello)"Artist: "Lorcan Pettigrew & The Oduya Priscilla"

• Original creativity
• Copyrighted images

```html
<!DOCTYPE html>
<html lang="en">
<head>
<meta charset="utf-8">
<title>Where The Quiet River Bends (Piano &amp; Cello) — Album Cover</title>
<link rel="stylesheet" href="https://fonts.googleapis.com/css2?family=Playfair+Display:wght@400;500&family=Tinos&display=swap">
<style>
  :root {
    --stage: #d6d6d6;
    --paper: #ffffff;
    --ink: #111111;
    --panel-dark: #0b0b0b;
    --panel-mid: #262626;
    --panel-glow: #8c8c8c;
    --panel-light: #ececec;
    --piano-black: #121212;
    --piano-grey: #3a3a3a;
    --piano-wood: #4a3a2c;
    --floor-shade: #dcdcdc;
    --ghost: #ececec;
  }
  * { box-sizing: border-box; margin: 0; padding: 0; }
  html, body { width: 1200px; height: 1200px; overflow: hidden; }
  body {
    background: var(--stage);
    position: relative;
    font-family: "Playfair Display", "Times New Roman", serif;
    color: var(--ink);
  }
  .cover {
    position: absolute;
    top: 330px;
    width: 540px;
    height: 540px;
    background: var(--paper);
    overflow: hidden;
    box-shadow: 0 2px 6px rgba(0,0,0,0.08);
  }
  .cover--panels { left: 40px; }
  .cover--feature { left: 620px; }

  .vertical {
    position: absolute;
    writing-mode: vertical-rl;
    transform: rotate(180deg);
    white-space: nowrap;
    line-height: 1;
  }
  .title {
    font-size: 46px;
    font-weight: 400;
    letter-spacing: -0.5px;
  }
  .subtitle {
    font-family: "Tinos", "Times New Roman", serif;
    font-size: 15px;
    letter-spacing: 0.95em;
  }
  .edition {
    font-family: "Tinos", "Times New Roman", serif;
    font-size: 10px;
    letter-spacing: 0.5em;
  }

  /* Panels cover */
  .photo-panel {
    position: absolute;
    top: 45px;
    height: 425px;
  }
  .photo-panel--left {
    left: 0;
    width: 200px;
    background: radial-gradient(ellipse 75% 45% at 45% 52%, var(--panel-light) 0%, var(--panel-glow) 22%, var(--panel-mid) 52%, var(--panel-dark) 80%);
  }
  .photo-panel--right {
    left: 326px;
    width: 214px;
    background: radial-gradient(ellipse 70% 42% at 62% 55%, var(--panel-light) 0%, var(--panel-glow) 22%, var(--panel-mid) 52%, var(--panel-dark) 80%);
  }
  .cover--panels .title { left: 212px; top: 58px; height: 412px; }
  .cover--panels .subtitle { left: 270px; top: 58px; height: 412px; }
  .cover--panels .edition { left: 296px; top: 58px; height: 412px; }

  .credit {
    position: absolute;
    font-family: "Tinos", "Times New Roman", serif;
    text-transform: uppercase;
    white-space: nowrap;
  }
  .credit__label { font-size: 7px; letter-spacing: 0.05em; }
  .credit__name { font-size: 9px; letter-spacing: 0.02em; }
  .cover--panels .credit--label { left: 0; width: 540px; top: 492px; text-align: center; }
  .cover--panels .credit--name { left: 0; width: 540px; top: 514px; text-align: center; }

  /* Feature cover */
  .ghost-title {
    position: absolute;
    left: -8px;
    top: 20px;
    height: 520px;
    writing-mode: vertical-rl;
    transform: rotate(180deg);
    font-size: 70px;
    line-height: 1;
    color: var(--ghost);
    white-space: nowrap;
  }
  .cover--feature .title { left: 72px; top: 62px; height: 412px; }
  .cover--feature .subtitle { left: 130px; top: 62px; height: 412px; }
  .cover--feature .edition { left: 156px; top: 62px; height: 412px; }
  .feature-photo {
    position: absolute;
    left: 190px;
    top: 110px;
    width: 350px;
    height: 330px;
    background:
      radial-gradient(ellipse 60% 50% at 68% 40%, var(--piano-wood) 0%, var(--piano-black) 35%, var(--piano-grey) 55%, rgba(255,255,255,0) 72%),
      radial-gradient(ellipse 70% 14% at 55% 88%, var(--floor-shade) 0%, rgba(255,255,255,0) 100%),
      var(--paper);
  }
  .cover--feature .credit--line {
    right: 24px;
    top: 512px;
    display: flex;
    align-items: baseline;
    gap: 6px;
  }
</style>
</head>
<body>

  <section class="cover cover--panels" aria-label="Album cover, panel layout">
    <div class="photo-panel photo-panel--left" role="img" aria-label="White grand piano lit on a dark stage, cropped view"></div>
    <div class="photo-panel photo-panel--right" role="img" aria-label="White grand piano with bench lit on a dark stage"></div>
    <h1 class="vertical title">WHERE THE QUIET</h1>
    <p class="vertical subtitle">RIVER BENDS</p>
    <p class="vertical edition">(PIANO &amp; CELLO)</p>
    <p class="credit credit--label credit__label">Artist:</p>
    <p class="credit credit--name credit__name">Lorcan Pettigrew &amp; The Oduya Priscilla</p>
  </section>

  <section class="cover cover--feature" aria-label="Album cover, feature layout">
    <div class="ghost-title" aria-hidden="true">WHERE THE QUIET</div>
    <div class="feature-photo" role="img" aria-label="Black grand piano with bench on a white background"></div>
    <h1 class="vertical title">WHERE THE QUIET</h1>
    <p class="vertical subtitle">RIVER BENDS</p>
    <p class="vertical edition">(PIANO &amp; CELLO)</p>
    <p class="credit credit--line">
      <span class="credit__label">Artist:</span>
      <span class="credit__name">Lorcan Pettigrew &amp; The Oduya Priscilla</span>
    </p>
  </section>

</body>
</html>
```